Landing Page for a new, High Production, farming technology

Brightfield Sprout
We need a single landing page, with an email signup for more information.
We build self-contained, farming boxes out of ISO containers. These containers use hydroponics and LED lighting to provide a year round growing environment for crops. So, you could grow crops anywhere at any time of the year in any environment.
For the purpose of this site, we will be doing split testing between several different themes using different sites and keywords.
This site's focus should be providing our product to people searching for high production farming technology.
We'll be focusing on the following key words: Agriculture, aquaponics, farm, garden, hydroponics, organic food, subsistence farming, urban farming, vertical garden.
Target Market(s)
We are going to be using this page to judge that
Number of Pages Required
1 page
Look and feel
Each slider illustrates characteristics of the customer's brand and the style your logo design should communicate.

```html
<!DOCTYPE html>
<html lang="en">
<head>
<meta charset="utf-8">
<title>Brightfield Sprout</title>
<link href="https://fonts.googleapis.com/css2?family=Montserrat:wght@800&family=Open+Sans:wght@400;600&display=swap" rel="stylesheet">
<style>
  :root {
    --orange: #dd9a56;
    --orange-soft: #e2aa6c;
    --panel: #f2f2f2;
    --ink: #2b2018;
    --footer: #2a2a2a;
    --footer-text: #a8a8a8;
    --white: #ffffff;
    --green-top: #86b85e;
    --green-mid: #9cc878;
    --green-low: #c3d9b2;
  }
  * { margin: 0; padding: 0; box-sizing: border-box; }
  html, body { width: 1200px; height: 759px; overflow: hidden; }
  body { font-family: "Open Sans", sans-serif; position: relative; background: var(--footer); }

  .hero-photo {
    position: absolute; inset: 0 0 auto 0; height: 680px;
    background: linear-gradient(180deg, var(--green-top) 0%, var(--green-mid) 55%, var(--green-low) 100%);
  }

  .top-bar {
    position: absolute; top: 0; left: 0; right: 0; height: 42px;
    background: linear-gradient(90deg, var(--orange) 0%, var(--orange-soft) 100%);
  }
  .main-nav {
    position: absolute; top: 0; right: 133px; height: 42px;
    display: flex; align-items: center; gap: 28px;
  }
  .main-nav a {
    font-size: 13.5px; font-weight: 600; color: var(--ink);
    text-decoration: none;
  }
  .main-nav a.is-active { text-decoration: underline; text-underline-offset: 3px; }

  .brand-panel {
    position: absolute; top: 0; left: 132px; width: 223px; height: 197px;
    background: var(--panel);
    display: flex; flex-direction: column; align-items: center; justify-content: center; gap: 14px;
  }
  .brand-mark { width: 40px; height: 40px; background: var(--orange); border-radius: 4px; }
  .brand-name {
    font-size: 15px; font-weight: 600; color: var(--orange);
    letter-spacing: 2px; text-transform: uppercase; text-align: center; line-height: 1.3;
  }

  .hero-copy {
    position: absolute; top: 141px; right: 132px; width: 520px; text-align: right;
  }
  .hero-title {
    font-family: "Montserrat", sans-serif; font-weight: 800;
    font-size: 31px; line-height: 40px; color: var(--white); letter-spacing: -0.5px;
  }
  .newsletter {
    margin: 12px 0 0 auto; width: 281px; height: 41px; background: var(--white);
    display: flex; align-items: center; justify-content: space-between; padding: 0 10px 0 17px;
  }
  .newsletter span { font-size: 13.5px; color: var(--ink); }

  .slider-arrow { position: absolute; top: 374px; width: 24px; height: 34px; }
  .slider-arrow.prev { left: 42px; }
  .slider-arrow.next { right: 42px; }

  .footer-wave { position: absolute; left: 0; top: 570px; }
  .footer-nav {
    position: absolute; left: 134px; top: 673px;
    font-size: 12px; color: var(--footer-text); display: flex; gap: 9px;
  }
  .footer-nav a { color: var(--footer-text); text-decoration: none; }
  .copyright { position: absolute; left: 134px; top: 707px; font-size: 12px; color: var(--footer-text); }
  .social { position: absolute; right: 133px; top: 688px; display: flex; gap: 7px; }
  .social span { width: 25px; height: 25px; border-radius: 50%; background: var(--orange); display: block; }
</style>
</head>
<body>
  <div class="hero-photo" role="img" aria-label="Photo: hand holding a freshly harvested head of lettuce above hydroponic growing rows"></div>

  <header class="top-bar">
    <nav class="main-nav">
      <a class="is-active" href="#">HOME</a>
      <a href="#">ABOUT US</a>
      <a href="#">SERVICES</a>
      <a href="#">WORKS</a>
      <a href="#">BLOG</a>
      <a href="#">CONTACT</a>
    </nav>
  </header>

  <div class="brand-panel">
    <span class="brand-mark"></span>
    <span class="brand-name">Brightfield<br>Sprout</span>
  </div>

  <section class="hero-copy">
    <h1 class="hero-title">WE BUILD SELF-CONTAINED,<br>FARMING BOXES OUT OF<br>ISO CONTAINERS</h1>
    <div class="newsletter">
      <span>Email Address for Newsletter</span>
      <svg width="25" height="20" viewBox="0 0 25 20" aria-hidden="true">
        <rect x="0" y="0" width="25" height="20" rx="3" fill="var(--orange)"/>
        <path d="M2 3 L12.5 11 L23 3" stroke="var(--white)" stroke-width="2" fill="none"/>
      </svg>
    </div>
  </section>

  <svg class="slider-arrow prev" viewBox="0 0 24 34" aria-label="Previous slide">
    <path d="M18 3 L6 17 L18 31" stroke="var(--white)" stroke-width="4" fill="none" stroke-linecap="round" stroke-linejoin="round"/>
  </svg>
  <svg class="slider-arrow next" viewBox="0 0 24 34" aria-label="Next slide">
    <path d="M6 3 L18 17 L6 31" stroke="var(--white)" stroke-width="4" fill="none" stroke-linecap="round" stroke-linejoin="round"/>
  </svg>

  <svg class="footer-wave" width="1200" height="189" viewBox="0 0 1200 189" aria-hidden="true">
    <path d="M0 86 C110 40 230 10 340 12 C520 16 650 92 840 92 C960 92 1080 60 1200 18 L1200 189 L0 189 Z" fill="var(--footer)"/>
  </svg>

  <footer>
    <nav class="footer-nav">
      <a href="#">Home</a><span>|</span>
      <a href="#">About Us</a><span>|</span>
      <a href="#">Services</a><span>|</span>
      <a href="#">Works</a><span>|</span>
      <a href="#">Blog</a><span>|</span>
      <a href="#">Contact</a>
    </nav>
    <p class="copyright">Copyright © 2018 Brightfield Sprout. All rights reserved.</p>
    <div class="social">
      <span aria-label="Social profile"></span>
      <span aria-label="Social profile"></span>
    </div>
  </footer>
</body>
</html>
```